International service dog training school needs web design

We need to upgrade our website. The website is https://brevantmoor.example/
We help trainers and service dog programs learn how to train service dogs with the latest and most ethical training methods. We offer online and in-person coaching services. We would like to see designs that are engaging and communicate professionalism, expertise, and care for the dogs and people we work with. Please also keep the colors already in the logo in the design.

```html
<!DOCTYPE html>
<html lang="en">
<head>
<meta charset="utf-8">
<title>Brevantmoor Center for Medical Assistance Canines</title>
<link href="https://fonts.googleapis.com/css2?family=Oswald:wght@400;500;600&family=Montserrat:ital,wght@0,400;0,500;0,600;1,400&display=swap" rel="stylesheet">
<style>
:root{
  --teal:#1a9e98;
  --teal-dark:#12807b;
  --blue:#2366ac;
  --navy:#1d4f86;
  --ink:#3b3f46;
  --muted:#6b7079;
  --aqua:#e3f5f7;
  --aqua-2:#d3eef3;
  --card:#eef8fb;
  --white:#ffffff;
}
*{box-sizing:border-box;margin:0;padding:0}
html,body{width:1200px;height:4800px;overflow:hidden;background:var(--white)}
body{font-family:"Montserrat",sans-serif;color:var(--ink);font-size:13px;line-height:1.65;position:relative}
h1,h2,h3,h4{font-family:"Oswald",sans-serif;font-weight:400}
.section{position:absolute;left:0;width:1200px;overflow:hidden}
.wrap{width:1000px;margin:0 auto;position:relative}
.eyebrow{font-family:"Oswald",sans-serif;font-size:13px;text-decoration:underline;color:var(--ink);letter-spacing:.3px;text-transform:uppercase}
.title{font-family:"Oswald",sans-serif;color:var(--blue);font-size:28px;text-transform:uppercase;letter-spacing:.3px;line-height:1.2}
.center{text-align:center}
.read{font-size:11px;color:var(--teal);font-weight:600;display:inline-block;border-bottom:1px solid var(--teal);padding:0 6px 4px;line-height:1.4}
.read::before{content:"";display:inline-block;width:9px;height:9px;border:1.5px solid var(--teal);border-radius:50%;margin-right:5px;vertical-align:-1px}
.btn{display:inline-block;background:var(--blue);color:var(--white);font-size:11px;font-weight:600;text-transform:uppercase;padding:9px 16px;border-radius:3px;line-height:1.4}
.btn::before{content:"";display:inline-block;width:9px;height:9px;border:1.5px solid var(--white);border-radius:50%;margin-right:6px;vertical-align:-1px}
.ph{background:linear-gradient(135deg,#b9a892,#6d6a5d)}

/* header */
.header{top:0;height:72px;background:var(--teal)}
.brand{position:absolute;left:0;top:0;height:72px;width:420px;background:var(--white);clip-path:polygon(0 0,100% 0,89% 100%,0 100%);display:flex;align-items:center;padding-left:40px;gap:12px}
.brand-dot{width:34px;height:34px;border-radius:50%;border:3px solid var(--blue);flex:none}
.brand-name{font-family:"Oswald",sans-serif;color:var(--blue);font-size:16px;line-height:1.15;text-transform:uppercase}
.nav{position:absolute;right:30px;top:0;height:72px;display:flex;align-items:center;gap:52px;font-family:"Oswald",sans-serif;color:var(--white);font-size:12px;text-transform:uppercase}

/* hero */
.hero{top:72px;height:520px;left:8px;width:1184px;background:linear-gradient(180deg,#33403a 0%,#4d5b4d 45%,#2f4a2c 100%)}
.hero-text{position:absolute;left:300px;top:185px;color:var(--white)}
.hero-text .kicker{font-family:"Oswald",sans-serif;font-size:17px;text-transform:uppercase}
.hero-text h1{font-size:38px;font-weight:600;line-height:1.2;text-transform:uppercase;margin-top:8px;letter-spacing:.5px}
.hero-btn{margin-top:22px;display:inline-flex;align-items:center;gap:22px;background:var(--teal);border-radius:20px;padding:5px 5px 5px 20px;font-size:10px;font-weight:600;text-transform:uppercase}
.hero-btn span.arrow{width:26px;height:26px;border-radius:50%;background:var(--white);display:flex;align-items:center;justify-content:center}
.socials{position:absolute;left:70px;top:210px;display:flex;flex-direction:column;gap:14px}
.socials i{width:9px;height:9px;border-radius:50%;background:var(--white);display:block}
.dots{position:absolute;left:60px;bottom:38px;display:flex;gap:10px}
.dots i{width:11px;height:11px;border-radius:50%;background:var(--white);display:block}
.dots i.on{background:var(--teal);box-shadow:0 0 0 3px rgba(255,255,255,.6)}
.arrows{position:absolute;right:60px;bottom:30px;display:flex;gap:10px}
.arrows span{width:28px;height:28px;border-radius:50%;background:var(--teal);display:flex;align-items:center;justify-content:center}
.scroll{position:absolute;right:70px;top:200px;width:2px;height:90px;background:rgba(255,255,255,.7)}

/* features */
.features{top:560px;height:140px;overflow:visible}
.features .wrap{display:flex;justify-content:center;gap:30px;padding-top:20px}
.feature{width:230px;height:100px;background:var(--card);position:relative;text-align:center;padding-top:58px}
.feature .ic{position:absolute;left:50%;top:-20px;margin-left:-32px;width:64px;height:64px;border-radius:50%;background:var(--teal);display:flex;align-items:center;justify-content:center}
.feature p{font-family:"Oswald",sans-serif;text-decoration:underline;font-size:14px}

/* about */
.about{top:720px;height:700px}
.about .wrap{display:flex;gap:40px}
.about-left{width:260px;text-align:center}
.about-left .title{font-size:24px;margin:14px 0 22px}
.about-photo{height:390px;background:linear-gradient(180deg,#e8ecef,#9aa3a8 60%,#6b6660)}
.founder{background:var(--card);padding:16px 16px 12px;margin-top:12px}
.founder h4{font-size:13px;line-height:1.1}
.founder p{font-style:italic;font-size:10.5px;color:var(--muted);line-height:1.7;margin-top:6px}
.about-right{flex:1;padding-top:4px}
.about-right p.body{font-size:12px;text-align:justify;line-height:1.75;color:var(--muted);margin-bottom:14px}
.about-right .more{text-align:right;margin-bottom:44px}
.mv{display:flex;gap:60px;margin-left:40px}
.mv-card{width:240px;background:var(--card);text-align:center;padding:44px 22px 22px;position:relative;border-radius:4px}
.mv-card .ic{position:absolute;left:50%;top:-30px;margin-left:-30px;width:60px;height:60px;border-radius:50%;background:var(--teal);display:flex;align-items:center;justify-content:center}
.mv-card h4{font-size:14px;text-decoration:underline}
.mv-card p{font-size:11.5px;color:var(--muted);margin-top:6px}
.stats{display:flex;gap:90px;margin:22px 0 0 60px;text-align:center}
.stat .ic{width:62px;height:62px;border-radius:50%;background:var(--teal);margin:0 auto 12px;display:flex;align-items:center;justify-content:center}
.stat strong{font-size:22px;font-weight:600;display:block;color:var(--ink);line-height:1.3}
.stat span{font-size:12px;color:var(--muted)}
.about-right .cta{text-align:right;margin-top:4px}

/* courses */
.courses{top:1440px;height:1060px;background:linear-gradient(180deg,#e9f8f8,#dcf1f6 50%,#cfe8f3)}
.courses .eyebrow{display:block;padding-top:46px}
.courses .title{margin:16px 0 40px;font-size:26px}
.grid3{display:grid;grid-template-columns:repeat(3,250px);justify-content:center;gap:30px 40px}
.course{text-align:center}
.ring{position:relative;width:160px;height:160px;margin:0 auto 14px}
.ring svg{position:absolute;left:0;top:0;width:100%;height:100%}
.ring .pic{position:absolute;inset:13px;border-radius:50%}
.course h4{font-size:14px;line-height:1.5}
.course p{font-size:11.5px;color:var(--muted);margin:6px 0 12px;line-height:1.6}
.row2{display:flex;justify-content:center;gap:50px;margin-top:30px}
.course-wide{display:flex;gap:18px;width:400px;text-align:left}
.course-wide .ring{margin:0;flex:none}
.course-wide .txt{padding-top:4px;display:flex;flex-direction:column;align-items:flex-start}
.course-wide h4{font-size:14px;line-height:1.5}
.course-wide p{font-size:11.5px;color:var(--muted);margin:6px 0 18px;line-height:1.6}
.courses .cta{text-align:right;margin-top:16px}

/* helping */
.helping{top:2500px;height:420px}
.helping .wrap{display:flex;gap:40px;padding-top:56px}
.help-left{width:220px;padding-top:40px;padding-left:20px}
.help-left .title{font-size:24px;margin-top:22px;text-align:left}
.help-cards{display:flex;gap:18px}
.help-card{width:230px;text-align:center}
.help-card .pic{height:110px}
.help-card h4{font-size:13.5px;margin-top:14px}
.help-card p{font-size:11.5px;color:var(--muted);margin:8px 10px 14px}
.helping .cta{position:absolute;right:0;top:345px}

/* research */
.research{top:2920px;height:500px;background:linear-gradient(180deg,#e6f6f6,#d8eef4)}
.research .eyebrow{display:block;padding-top:40px}
.research .title{font-size:26px;margin-top:12px}
.research .sub{font-family:"Oswald",sans-serif;font-size:12px;color:var(--blue);text-transform:uppercase;margin-top:8px}
.research .lead{font-size:11.5px;color:var(--muted);margin:14px 60px 22px;text-align:center}
.research-cards{display:flex;justify-content:center;gap:36px}
.r-card{width:250px;text-align:center}
.r-card .pic{height:120px}
.r-card h4{font-size:13.5px;margin:12px 0 12px;line-height:1.3;min-height:36px}
.research .cta{position:absolute;right:0;top:440px}

/* testimonial */
.testi{top:3420px;height:420px}
.testi .wrap{display:flex;gap:70px;padding-top:60px}
.testi-ring{position:relative;width:270px;height:270px;flex:none;margin-left:20px}
.testi-ring svg{position:absolute;left:0;top:0;width:100%;height:100%}
.testi-ring .pic{position:absolute;inset:14px;border-radius:50%;background:linear-gradient(135deg,#8a6a4a,#d8c6b3)}
.testi-body{flex:1;text-align:center}
.testi-body .title{font-size:26px;margin:14px 0 22px}
.quote{background:var(--card);padding:18px 30px;font-style:italic;font-size:12px;color:var(--muted);line-height:1.7;border-radius:4px}
.author{display:flex;align-items:center;justify-content:center;gap:16px;margin-top:20px}
.author .av{width:64px;height:64px;border-radius:50%;background:linear-gradient(135deg,#e7d3b6,#b79a78)}
.author strong{display:block;font-size:11px;text-align:left}
.author span{font-size:10px;color:var(--muted)}
.tdots{display:flex;justify-content:center;gap:6px;margin-top:18px}
.tdots i{width:5px;height:5px;border-radius:50%;background:#c3c8cc;display:block}
.tdots i.on{background:var(--blue)}
.testi .cta{position:absolute;right:0;top:370px}

/* gallery */
.gallery{top:3840px;height:410px;background:#f4fafc}
.gallery .eyebrow{display:block;padding-top:36px}
.gallery .title{font-size:26px;margin:16px 0 26px}
.gal{display:flex;justify-content:center}
.gal div{width:180px;height:260px}

/* cta band */
.talk{top:4250px;height:200px;overflow:visible}
.talk .wrap{text-align:center;padding-top:46px;padding-right:140px}
.talk h2{font-size:32px;color:var(--blue);line-height:1.3}
.talk p{font-size:11.5px;color:var(--ink);width:440px;margin:8px auto 14px}
.talk .call{font-weight:600;font-size:17px;line-height:1.2}
.dog{position:absolute;right:110px;top:-40px;width:150px;height:200px;border-radius:40% 40% 12% 12%;background:linear-gradient(180deg,#2a2420,#6b4a32 60%,#e8e2d8)}

/* footer */
.footer{top:4450px;height:350px;background:linear-gradient(180deg,#e3f5f7,#d2ecf3)}
.footer .wrap{display:flex;gap:40px;padding-top:40px}
.f-brand{width:240px}
.f-brand .brand-row{display:flex;gap:10px;align-items:center}
.f-brand p{font-size:10.5px;color:var(--muted);margin-top:12px;line-height:1.6}
.f-social{display:flex;gap:8px;margin-top:16px;padding-left:40px}
.f-social i{width:22px;height:22px;border-radius:50%;background:var(--blue);display:block}
.f-col{width:160px}
.f-col h4{font-size:13px;text-decoration:underline;margin-bottom:12px}
.f-col li{list-style:none;font-size:11px;color:var(--muted);line-height:1.35;margin-bottom:6px}
.f-col li.on{color:var(--teal)}
.f-contact{width:220px}
.f-contact h4{font-size:13px;text-decoration:underline;margin-bottom:12px}
.map{height:80px;background:linear-gradient(135deg,#eef0ea,#d9e2e4)}
.f-line{display:flex;gap:10px;align-items:center;font-size:10.5px;color:var(--muted);margin-top:14px;line-height:1.4}
</style>
</head>
<body>

<header class="section header">
  <div class="brand"><span class="brand-dot"></span><div class="brand-name">Marissa Vell Ph.D.<br>Brevantmoor Center for<br>Medical Assistance Canines</div></div>
  <nav class="nav"><span>Home</span><span>The Center</span><span>Helping Organizations</span><span>Teaching Trainers</span><span>Research</span><span>Contact</span></nav>
</header>

<section class="section hero" role="img" aria-label="Three trainers in club jackets holding small dogs on a training field">
  <div class="socials"><i></i><i></i><i></i></div>
  <div class="hero-text">
    <div class="kicker">Welcome to Brevantmoor Center for Medical Assistance Canines</div>
    <h1>We provide coaching for<br>service dog professionals</h1>
    <div class="hero-btn">Contact Us <span class="arrow"><svg width="12" height="10" viewBox="0 0 12 10"><path d="M1 5h9M6 1l4 4-4 4" stroke="#1a9e98" stroke-width="1.8" fill="none"/></svg></span></div>
  </div>
  <div class="scroll"></div>
  <div class="dots"><i></i><i></i><i class="on"></i><i></i><i></i></div>
  <div class="arrows">
    <span><svg width="10" height="10" viewBox="0 0 10 10"><path d="M6.5 1.5 3 5l3.5 3.5" stroke="#fff" stroke-width="1.6" fill="none"/></svg></span>
    <span><svg width="10" height="10" viewBox="0 0 10 10"><path d="M3.5 1.5 7 5 3.5 8.5" stroke="#fff" stroke-width="1.6" fill="none"/></svg></span>
  </div>
</section>

<section class="section features">
  <div class="wrap">
    <div class="feature"><span class="ic"><svg width="28" height="28" viewBox="0 0 28 28"><circle cx="14" cy="14" r="9" fill="none" stroke="#fff" stroke-width="2.5"/><path d="M9 14l3.5 3.5L19 11" stroke="#fff" stroke-width="2.5" fill="none"/></svg></span><p>Train a dog</p></div>
    <div class="feature"><span class="ic"><svg width="28" height="28" viewBox="0 0 28 28"><path d="M4 16l6-6 4 4 4-4 6 6-6 6-4-4-4 4z" fill="#fff"/></svg></span><p>Help a person</p></div>
    <div class="feature"><span class="ic"><svg width="28" height="28" viewBox="0 0 28 28"><path d="M14 23S5 17 5 11a4.5 4.5 0 0 1 9-1 4.5 4.5 0 0 1 9 1c0 6-9 12-9 12z" fill="#fff"/></svg></span><p>Be the difference</p></div>
  </div>
</section>

<section class="section about">
  <div class="wrap">
    <div class="about-left">
      <span class="eyebrow">About Us</span>
      <h2 class="title">Who we are?</h2>
      <div class="about-photo" role="img" aria-label="Founder walking a service dog on a lead through a bright hallway"></div>
      <div class="founder">
        <h4>Marissa Vell<br>Ph.D. Founder</h4>
        <p>“Training service dogs is a rewarding career for those who care about dogs and people. It requires empathy, dedication, precision, and a great deal of knowledge in dog behavior and psychology.”</p>
      </div>
    </div>
    <div class="about-right">
      <p class="body">The Brevantmoor Center for Medical Assistance Canines was founded by Marissa Vell Ph.D. in response to demand for coaching from dog trainers, medical professionals, and service dog programs. Marissa Vell Ph.D. has helped hundreds of trainers and several programs both in the US and internationally, expand the type of dogs they could offer to include medical alert dogs. Specialized mostly in the training of diabetic alert dogs, seizure dogs, and psychiatric service dogs, Marissa Vell is also experienced in the training of mobility assistance dogs and autism dogs. The coaching is individually catered to meet the programs’ needs.</p>
      <p class="body">With a focus on science-based, ethical, and force-free training methods, the center provides cutting-edge training methods when working with medical assistance dogs.</p>
      <div class="more"><span class="read">Read More</span></div>
      <div class="mv">
        <div class="mv-card"><span class="ic"><svg width="26" height="26" viewBox="0 0 26 26"><path d="M6 20l4-10 10-4-4 10z" fill="none" stroke="#fff" stroke-width="2"/><circle cx="13" cy="13" r="2" fill="#fff"/></svg></span><h4>Mission</h4><p>Lorem ipsum dolor sit amet, consectetur adipiscing elit. Ut elit tellus, luctus nec ullamcorper mattis, pulvinar dapibus leo.</p></div>
        <div class="mv-card"><span class="ic"><svg width="26" height="26" viewBox="0 0 26 26"><circle cx="13" cy="13" r="9" fill="none" stroke="#fff" stroke-width="2"/><circle cx="13" cy="13" r="4.5" fill="none" stroke="#fff" stroke-width="2"/><circle cx="13" cy="13" r="1.5" fill="#fff"/></svg></span><h4>Vission</h4><p>Lorem ipsum dolor sit amet, consectetur adipiscing elit. Ut elit tellus, luctus nec ullamcorper mattis, pulvinar dapibus leo.</p></div>
      </div>
      <div class="stats">
        <div class="stat"><span class="ic"><svg width="26" height="26" viewBox="0 0 26 26"><circle cx="10" cy="9" r="3.5" fill="none" stroke="#fff" stroke-width="2"/><circle cx="17" cy="10" r="3" fill="none" stroke="#fff" stroke-width="2"/><path d="M3 20c1-4 4-6 7-6s6 2 7 6M16 15c3 0 5 2 6 5" fill="none" stroke="#fff" stroke-width="2"/></svg></span><strong>1,160+</strong><span>Happy Clients</span></div>
        <div class="stat"><span class="ic"><svg width="26" height="26" viewBox="0 0 26 26"><circle cx="13" cy="9" r="4" fill="none" stroke="#fff" stroke-width="2"/><path d="M5 22c1-5 4-7 8-7s7 2 8 7" fill="none" stroke="#fff" stroke-width="2"/></svg></span><strong>160+</strong><span>Trainer</span></div>
        <div class="stat"><span class="ic"><svg width="26" height="26" viewBox="0 0 26 26"><circle cx="13" cy="13" r="8" fill="none" stroke="#fff" stroke-width="2"/><path d="M9 15c1 2 2.5 3 4 3s3-1 4-3" fill="none" stroke="#fff" stroke-width="2"/></svg></span><strong>1,160+</strong><span>Happy Clients</span></div>
      </div>
      <div class="cta"><span class="btn">Know More About Us</span></div>
    </div>
  </div>
</section>

<section class="section courses">
  <div class="wrap center">
    <span class="eyebrow">Courses</span>
    <h2 class="title">Your journey as a medical assistance dog trainer starts here</h2>
    <div class="grid3">
      <div class="course"><div class="ring"><svg viewBox="0 0 190 190"><circle cx="95" cy="95" r="90" fill="none" stroke="#1a9e98" stroke-width="6" stroke-dasharray="300 265" transform="rotate(-150 95 95)"/></svg><div class="pic ph" role="img" aria-label="Brown shepherd dog standing beside its handler"></div></div><h4>Full Curriculum</h4><p>Learn everything you need to become a professional service dog trainer and specialize in medical alert dogs. This</p><span class="read">Read More</span></div>
      <div class="course"><div class="ring"><svg viewBox="0 0 190 190"><circle cx="95" cy="95" r="90" fill="none" stroke="#1a9e98" stroke-width="6" stroke-dasharray="300 265" transform="rotate(-150 95 95)"/></svg><div class="pic ph" role="img" aria-label="Candidate dog resting in an indoor kennel"></div></div><h4>Service Dog Candidate Selection</h4><p>Learn everything you need to become a professional service dog trainer and specialize in medical alert dogs. This</p><span class="read">Read More</span></div>
      <div class="course"><div class="ring"><svg viewBox="0 0 190 190"><circle cx="95" cy="95" r="90" fill="none" stroke="#1a9e98" stroke-width="6" stroke-dasharray="300 265" transform="rotate(-150 95 95)"/></svg><div class="pic" style="background:linear-gradient(135deg,#9fb3c9,#5e6b7a)" role="img" aria-label="Trainers in a classroom assessment session"></div></div><h4>Service Dog Training And Assessments</h4><p>Learn everything you need to become a professional service dog trainer and specialize in medical alert dogs. This</p><span class="read">Read More</span></div>
      <div class="course"><div class="ring"><svg viewBox="0 0 190 190"><circle cx="95" cy="95" r="90" fill="none" stroke="#1a9e98" stroke-width="6" stroke-dasharray="300 265" transform="rotate(-150 95 95)"/></svg><div class="pic ph" role="img" aria-label="Handlers practising tasks with dogs indoors"></div></div><h4>Medical Assistant Dog Tasks</h4><p>Learn everything you need to become a professional service dog trainer and specialize in medical alert dogs. This</p><span class="read">Read More</span></div>
      <div class="course"><div class="ring"><svg viewBox="0 0 190 190"><circle cx="95" cy="95" r="90" fill="none" stroke="#1a9e98" stroke-width="6" stroke-dasharray="300 265" transform="rotate(-150 95 95)"/></svg><div class="pic" style="background:linear-gradient(135deg,#c9c4bb,#7c7468)" role="img" aria-label="Service dog walking through a busy public hall"></div></div><h4>Public Access</h4><p>Learn everything you need to become a professional service dog trainer and specialize in medical alert dogs. This</p><span class="read">Read More</span></div>
      <div class="course"><div class="ring"><svg viewBox="0 0 190 190"><circle cx="95" cy="95" r="90" fill="none" stroke="#1a9e98" stroke-width="6" stroke-dasharray="300 265" transform="rotate(-150 95 95)"/></svg><div class="pic ph" role="img" aria-label="Client sitting on the floor with a dog"></div></div><h4>The Clients</h4><p>Learn everything you need to become a professional service dog trainer and specialize in medical alert dogs. This</p><span class="read">Read More</span></div>
    </div>
    <div class="row2">
      <div class="course-wide"><div class="ring"><svg viewBox="0 0 190 190"><circle cx="95" cy="95" r="90" fill="none" stroke="#1a9e98" stroke-width="6" stroke-dasharray="300 265" transform="rotate(-150 95 95)"/></svg><div class="pic" style="background:linear-gradient(135deg,#a9b6a6,#6a7566)" role="img" aria-label="Group of trainers with dogs at an outside facility"></div></div><div class="txt"><h4>In-Person Teaching At Your Facility</h4><p>Learn everything you need to become a professional service dog trainer and specialize in medical alert dogs. This</p><span class="read">Read More</span></div></div>
      <div class="course-wide"><div class="ring"><svg viewBox="0 0 190 190"><circle cx="95" cy="95" r="90" fill="none" stroke="#1a9e98" stroke-width="6" stroke-dasharray="300 265" transform="rotate(-150 95 95)"/></svg><div class="pic ph" role="img" aria-label="Students training dogs inside the center"></div></div><div class="txt"><h4>In-Person Learning At Our Facility</h4><p>Learn everything you need to become a professional service dog trainer and specialize in medical alert dogs. This</p><span class="read">Read More</span></div></div>
    </div>
    <div class="cta"><span class="btn">Check All Our Courses</span></div>
  </div>
</section>

<section class="section helping">
  <div class="wrap">
    <div class="help-left">
      <span class="eyebrow">Helping Organizations</span>
      <h2 class="title">Professional coaching for your service dog organization</h2>
    </div>
    <div class="help-cards">
      <div class="help-card"><div class="pic" style="background:linear-gradient(135deg,#d9d6d0,#8f8a80)" role="img" aria-label="Trainer on a video call at a laptop"></div><h4>Phone/Video Consultation</h4><p>Learn everything you need to become a professional service dog trainer and specialize in medical alert dogs. This</p><span class="read">Read More</span></div>
      <div class="help-card"><div class="pic" style="background:linear-gradient(135deg,#c7ccd2,#6f7782)" role="img" aria-label="Audience attending a seminar presentation"></div><h4>Seminar/Presentations</h4><p>Learn everything you need to become a professional service dog trainer and specialize in medical alert dogs. This</p><span class="read">Read More</span></div>
      <div class="help-card"><div class="pic" style="background:linear-gradient(135deg,#8d9c6e,#4f5a3a)" role="img" aria-label="Handlers working with dogs on a grass field"></div><h4>Online Or In Person Consulting</h4><p>Learn everything you need to become a professional service dog trainer and specialize in medical alert dogs. This</p><span class="read">Read More</span></div>
    </div>
    <span class="btn cta">Know More</span>
  </div>
</section>

<section class="section research">
  <div class="wrap center">
    <span class="eyebrow">Research</span>
    <h2 class="title">Medical detection dogs - research projects</h2>
    <div class="sub">Expertise and collaboration with your research projects</div>
    <p class="lead">Marissa Vell Ph.D. is involved in different research projects in the area of medical detection dogs. She has been at the forefront of canine medical detection research and development projects. Her work involves proving the ability of dogs to detect the scent of hypoglycemic episodes as well as seizures.</p>
    <div class="research-cards">
      <div class="r-card"><div class="pic" style="background:linear-gradient(135deg,#e9eef2,#8aa2b6)" role="img" aria-label="Veterinarian examining a dog in a clinic"></div><h4>Expertise And Collaboration With Your Research Projects</h4><span class="read">Read More</span></div>
      <div class="r-card"><div class="pic" style="background:linear-gradient(135deg,#2c3a5a,#3f6b3a)" role="img" aria-label="Dog working on a path integration exercise in an arena"></div><h4>Path Integration In Dogs</h4><span class="read">Read More</span></div>
      <div class="r-card"><div class="pic" style="background:linear-gradient(135deg,#b08a5e,#4a3a2c)" role="img" aria-label="Handler seated on steps with a dog"></div><h4>Blindfolded Dogs Relocate A Target Through Path Integration</h4><span class="read">Read More</span></div>
    </div>
    <span class="btn cta">Read More</span>
  </div>
</section>

<section class="section testi">
  <div class="wrap">
    <div class="testi-ring"><svg viewBox="0 0 270 270"><circle cx="135" cy="135" r="130" fill="none" stroke="#1a9e98" stroke-width="7" stroke-dasharray="460 357" transform="rotate(40 135 135)"/></svg><div class="pic" role="img" aria-label="Client portrait with her dog"></div></div>
    <div class="testi-body">
      <span class="eyebrow">Testimony</span>
      <h2 class="title">Check what our client say</h2>
      <div class="quote">“Lorem ipsum dolor sit amet, consectetur adipiscing elit, sed do eiusmod tempor incididunt ut labore et dolore magna aliqua. Vulputate dignissim suspendisse in est ante. Faucibus turpis in eu mi bibendum neque. Sodales ut etiam sit amet nisl purus. Velit laoreet id donec ultrices tincidunt.”</div>
      <div class="author"><div class="av" role="img" aria-label="Client portrait"></div><div><strong>Aaron Pell</strong><span>CEO</span></div></div>
      <div class="tdots"><i></i><i></i><i></i><i></i><i class="on"></i></div>
    </div>
    <span class="btn cta">Know More</span>
  </div>
</section>

<section class="section gallery">
  <div class="wrap center">
    <span class="eyebrow">Portfolio</span>
    <h2 class="title">Check our gallery</h2>
    <div class="gal">
      <div style="background:linear-gradient(180deg,#3a4a2c,#8a6a3a)" role="img" aria-label="Trainer kneeling with small dogs on grass"></div>
      <div style="background:linear-gradient(180deg,#203a66,#1c2a44)" role="img" aria-label="Handler with a shepherd dog at night"></div>
      <div style="background:linear-gradient(180deg,#5a6a74,#b8a890)" role="img" aria-label="Man crouching beside a fluffy dog outdoors"></div>
      <div style="background:linear-gradient(180deg,#d89a3a,#7a5a2a)" role="img" aria-label="Dog in autumn leaves"></div>
      <div style="background:linear-gradient(180deg,#9ab0cc,#3a5a3a)" role="img" aria-label="Woman holding a treat for a dog in a park"></div>
    </div>
  </div>
</section>

<section class="section talk">
  <div class="dog" role="img" aria-label="Tricolour mountain dog sitting"></div>
  <div class="wrap">
    <h2>Want to talk to an expert?</h2>
    <p>Lorem ipsum dolor sit amet, consectetur adipiscing elit. Ut elit tellus, luctus nec ullamcorper mattis, pulvinar dapibus.</p>
    <div class="call">Call Us Now<br>+1 0100 555 0142</div>
  </div>
</section>

<footer class="section footer">
  <div class="wrap">
    <div class="f-brand">
      <div class="brand-row"><span class="brand-dot"></span><div class="brand-name" style="font-size:13px">Marissa Vell Ph.D.<br>Brevantmoor Center for<br>Medical Assistance Canines</div></div>
      <p>Lorem ipsum dolor sit amet, consectetur adipiscing elit, sed do eiusmod tempor incididunt ut labore et dolore magna aliqua. Vulputate dignissim suspendisse in est ante.</p>
      <div class="f-social"><i></i><i></i><i></i></div>
    </div>
    <div class="f-col"><h4>Our Company</h4><ul><li class="on">Home</li><li>The Center</li><li>Helping organizations</li><li>Teaching Trainers</li><li>Research</li><li>Contact</li></ul></div>
    <div class="f-col"><h4>Our Courses</h4><ul><li>Full Curriculum</li><li>Service Dog Candidate Selection</li><li>Service Dog Training And Assessments</li><li>Medical Assistant Dog Tasks</li><li>Public Access</li><li>The Clients</li><li>In-Person Teaching At Your Facility</li><li>In-Person Learning At Our Facility</li></ul></div>
    <div class="f-contact"><h4>Contact Us</h4>
      <div class="map" role="img" aria-label="Street map showing the center's location"></div>
      <div class="f-line"><svg width="14" height="16" viewBox="0 0 14 16"><path d="M7 15s5-5 5-9A5 5 0 0 0 2 6c0 4 5 9 5 9z" fill="none" stroke="#1a9e98" stroke-width="1.6"/><circle cx="7" cy="6" r="1.8" fill="#1a9e98"/></svg><span>418 Larkfield Rd<br>Dunmore, OH 45000</span></div>
      <div class="f-line"><svg width="14" height="12" viewBox="0 0 14 12"><rect x="1" y="1" width="12" height="10" rx="1" fill="none" stroke="#1a9e98" stroke-width="1.5"/><path d="M1 2l6 5 6-5" fill="none" stroke="#1a9e98" stroke-width="1.5"/></svg><span>info@brevantmoor.example</span></div>
      <div class="f-line"><svg width="14" height="14" viewBox="0 0 14 14"><path d="M3 1l3 3-1.5 2a8 8 0 0 0 3.5 3.5L10 8l3 3-2 2C6 13 1 8 1 3z" fill="none" stroke="#1a9e98" stroke-width="1.5"/></svg><span>+1 0100 555 0142</span></div>
    </div>
  </div>
</footer>

</body>
</html>
```